International Film making Business needs the 5 Logos provided made into a POSTER Format

Design Task:
CREATE A POSTER DESIGN USING THE 5 LOGOS PROVIDED. The GLAD SKY VISTA LOGO should stand out from the others by being in the middle with the other 4 logos connected to it somehow.

The 5 Businesses already has their 5 Logos, all similar in design to each other.

GLAD SKY VISTA is the Main Logo that encompasses the other 4 Logos. So it must stand out more and it is like the Overall Business entity that incorporates the other 4 Logos.

What is required is that by using the 5 Logo designs provided, create a cool graphic artwork that somehow incorporates ALL of the 5 Logos - But having the GLAD SKY VISTA Logo at the forefront/most important/standing out the most.
- GLAD SKY VISTA will probably be bigger than the others
- and could be changed into 3D.

I have attached all 5 logos and a hand drawn example of how the GLAD SKY VISTAS could stand out from the rest.

THE DESIGNS OF THE LOGOS SHOULD NOT BE CHANGED (except the GLADSKYVISTA which can be 3D)

Please do not be restricted with the sample idea. Creativity is encouraged

DIMENSION: 3000 mm x 6000 mm
high resolution graphic

Logo Text

glad sky , glad sky reels, glad sky tales, glad sky groovy, GLAD SKY VISTAS

Requirements
Must have
• USE THE 5 LOGOS PROVIDED ONLY - Only GLAD SKY VISTA can be changed into 3D only
Nice to have
• Eye catching design, showing the Glad Sky Vista as the most powerful Logo that has the other 4 as subordinate companies
Should not have
• ANY CHANGE IN THE 5 LOGO DESIGNS (EXcept 3D for Glad Sky Vistas)

```html
<!DOCTYPE html>
<html lang="en">
<head>
<meta charset="utf-8">
<title>Glad Sky Vistas – Group Poster</title>
<link rel="stylesheet" href="https://fonts.googleapis.com/css2?family=Cinzel:wght@600&family=Questrial&display=swap">
<style>
  :root {
    --ink: #000000;
    --gold: #b07f2c;
    --gold-light: #f4dd92;
    --gold-deep: #8f6420;
    --silver: #9c9c9c;
    --paper: #ffffff;
    --brand-blue: #1f86cf;
    --brand-black: #1b1b1b;
    --brand-purple: #5b2d8e;
    --brand-green: #1f8a3c;
  }
  html, body {
    margin: 0;
    padding: 0;
    width: 1200px;
    height: 600px;
    overflow: hidden;
    background: var(--ink);
  }
  .poster {
    display: block;
    width: 1200px;
    height: 600px;
  }
  .wordmark {
    font-family: "Cinzel", "Times New Roman", serif;
    font-weight: 600;
    fill: var(--gold);
  }
  .web-address {
    font-family: "Questrial", "Century Gothic", sans-serif;
    fill: var(--silver);
  }
  .division-name {
    font-family: "Cinzel", "Times New Roman", serif;
    font-weight: 600;
  }
  .division--sky    { fill: var(--brand-blue); }
  .division--reels  { fill: var(--brand-black); }
  .division--tales  { fill: var(--brand-purple); }
  .division--groovy { fill: var(--brand-green); }
  .gold-frame  { fill: url(#goldFrame); }
  .white-field { fill: var(--paper); }
</style>
</head>
<body>
<svg class="poster" viewBox="0 0 1200 600" xmlns="http://www.w3.org/2000/svg">
  <defs>
    <linearGradient id="goldFrame" x1="0" y1="1" x2="1" y2="0">
      <stop offset="0" stop-color="var(--gold-deep)"/>
      <stop offset="0.3" stop-color="var(--gold)"/>
      <stop offset="0.5" stop-color="var(--gold-light)"/>
      <stop offset="0.7" stop-color="var(--gold)"/>
      <stop offset="1" stop-color="var(--gold-deep)"/>
    </linearGradient>
    <linearGradient id="bandBlue" x1="0" y1="0" x2="1" y2="0">
      <stop offset="0" stop-color="#27388d"/>
      <stop offset="0.45" stop-color="#1aa7e1"/>
      <stop offset="1" stop-color="#2a3c93"/>
    </linearGradient>
    <linearGradient id="bandGrey" x1="0" y1="0" x2="1" y2="0">
      <stop offset="0" stop-color="#0f0f0f"/>
      <stop offset="0.6" stop-color="#7a7a7c"/>
      <stop offset="1" stop-color="#1c1c1c"/>
    </linearGradient>
    <linearGradient id="bandSpectrum" x1="0" y1="0" x2="1" y2="0">
      <stop offset="0" stop-color="#5c2d8f"/>
      <stop offset="0.2" stop-color="#2b2f7f"/>
      <stop offset="0.45" stop-color="#1b9bd7"/>
      <stop offset="0.65" stop-color="#3cb54a"/>
      <stop offset="0.85" stop-color="#fff200"/>
      <stop offset="1" stop-color="#f26522"/>
    </linearGradient>
    <linearGradient id="bandGreen" x1="0" y1="0" x2="1" y2="0">
      <stop offset="0" stop-color="#0c6b39"/>
      <stop offset="0.5" stop-color="#8dc63f"/>
      <stop offset="1" stop-color="#0e6a39"/>
    </linearGradient>
  </defs>

  <!-- header band -->
  <rect class="header-band" x="0" y="0" width="1200" height="290" fill="var(--ink)"/>

  <!-- main brand: plain mark + name -->
  <circle class="brand-disc" cx="482" cy="150" r="64" fill="var(--gold)"/>
  <text class="wordmark" x="592" y="130" font-size="92" textLength="480" lengthAdjust="spacing">GLAD SKY</text>
  <text class="wordmark" x="592" y="217" font-size="92" textLength="480" lengthAdjust="spacing">VISTAS</text>
  <text class="web-address" x="592" y="255" font-size="36" textLength="480" lengthAdjust="spacing">gladskyvistas.com.au</text>

  <!-- division colour bands -->
  <rect x="0"   y="290" width="318" height="310" fill="url(#bandBlue)"/>
  <rect x="318" y="290" width="287" height="310" fill="url(#bandGrey)"/>
  <rect x="605" y="290" width="285" height="310" fill="url(#bandSpectrum)"/>
  <rect x="890" y="290" width="310" height="310" fill="url(#bandGreen)"/>

  <!-- division: glad sky -->
  <g class="division-tile">
    <polygon class="gold-frame" points="169,290 327,445 169,600 11,445"/>
    <polygon class="white-field" points="169,313 303,445 169,577 35,445"/>
    <circle cx="105" cy="445" r="10" fill="var(--brand-blue)"/>
    <text class="division-name division--sky" x="182" y="440" font-size="30" text-anchor="middle">GLAD</text>
    <text class="division-name division--sky" x="182" y="474" font-size="30" text-anchor="middle">SKY</text>
  </g>

  <!-- division: glad sky reels -->
  <g class="division-tile">
    <polygon class="gold-frame" points="456,290 614,445 456,600 298,445"/>
    <polygon class="white-field" points="456,313 590,445 456,577 322,445"/>
    <circle cx="384" cy="445" r="10" fill="var(--brand-black)"/>
    <text class="division-name division--reels" x="466" y="430" font-size="22" text-anchor="middle">GLAD SKY</text>
    <text class="division-name division--reels" x="466" y="464" font-size="30" text-anchor="middle">REELS</text>
  </g>

  <!-- division: glad sky tales -->
  <g class="division-tile">
    <polygon class="gold-frame" points="743,290 901,445 743,600 585,445"/>
    <polygon class="white-field" points="743,313 877,445 743,577 609,445"/>
    <circle cx="671" cy="445" r="10" fill="var(--brand-purple)"/>
    <text class="division-name division--tales" x="753" y="430" font-size="22" text-anchor="middle">GLAD SKY</text>
    <text class="division-name division--tales" x="753" y="464" font-size="30" text-anchor="middle">TALES</text>
  </g>

  <!-- division: glad sky groovy -->
  <g class="division-tile">
    <polygon class="gold-frame" points="1031,290 1189,445 1031,600 873,445"/>
    <polygon class="white-field" points="1031,313 1165,445 1031,577 897,445"/>
    <circle cx="1031" cy="395" r="12" fill="var(--brand-green)"/>
    <text class="division-name division--groovy" x="1031" y="465" font-size="22" text-anchor="middle">GLAD SKY</text>
    <text class="division-name division--groovy" x="1031" y="500" font-size="30" text-anchor="middle">GROOVY</text>
  </g>
</svg>
</body>
</html>
```